Online medical reviews website needs banner advert!

We need banner advert templates for our website, www.traineepanel.net. These should meet the technical requirements of our partner (uploaded).

Our groundbreaking website allows doctors in training to rate and review their training.

The adverts should use the same modern design language and colour scheme as our website. They should use the text 'Help a junior doctor make a big decision - rate your training!'.

Vector assets should be supplied, allowing us to use alternative text in future.
Updates

Industry/Entity Type

Healthcare

Font styles to use
Other font styles liked:
• Karla

Colors
3277b5
0555a3
ffffff

Requirements
Must have
• Similar design to our website. Should be elegant & modern. Must allow future text to be easily inserted.
Should not have
• Unrelated design.

```html
<!DOCTYPE html>
<html lang="en">
<head>
<meta charset="utf-8">
<title>Rate Your Training Banner</title>
<link rel="stylesheet" href="https://fonts.googleapis.com/css2?family=Open+Sans:wght@500;700&display=swap">
<style>
  :root {
    --blue-deep: #0555a3;
    --blue-mid: #3277b5;
    --blue-light: #6ccdf0;
    --white: #ffffff;
    --canvas-bg: #e9eaec;
  }
  html, body {
    margin: 0;
    padding: 0;
    width: 1200px;
    height: 1200px;
    overflow: hidden;
    background: var(--canvas-bg);
  }
  .canvas {
    position: relative;
    width: 1200px;
    height: 1200px;
  }
  .banner {
    position: absolute;
    left: 53px;
    top: 348px;
    width: 1094px;
    height: 503px;
    overflow: hidden;
    font-family: "Open Sans", Arial, sans-serif;
    color: var(--white);
  }
  .banner-art {
    position: absolute;
    inset: 0;
    width: 100%;
    height: 100%;
  }
  .headline {
    position: absolute;
    left: 55px;
    top: 88px;
    margin: 0;
    font-weight: 700;
    line-height: 1;
    text-transform: uppercase;
  }
  .headline span { display: block; }
  .headline .lead { font-size: 43px; margin-bottom: 10px; }
  .headline .line { font-size: 28px; margin-bottom: 12px; }
  .headline .big { font-size: 78px; letter-spacing: 12px; margin: 2px 0 10px; }
  .tagline {
    position: absolute;
    left: 55px;
    top: 404px;
    margin: 0;
    font-size: 23px;
    font-weight: 500;
  }
  .rating {
    position: absolute;
    left: 74px;
    top: 442px;
    display: flex;
    gap: 3px;
  }
  .rating svg { width: 34px; height: 34px; }
  .cta-button {
    position: absolute;
    left: 616px;
    top: 433px;
    width: 433px;
    height: 49px;
    background: var(--blue-deep);
    border-radius: 3px;
    display: flex;
    align-items: center;
    justify-content: center;
    font-size: 22px;
    font-weight: 500;
  }
</style>
</head>
<body>
<div class="canvas">
  <section class="banner">
    <svg class="banner-art" viewBox="0 0 912 419" preserveAspectRatio="none" aria-hidden="false">
      <defs>
        <linearGradient id="panel-gradient" x1="0" y1="0" x2="1" y2="0">
          <stop offset="0" stop-color="#3a80c0"/>
          <stop offset="0.35" stop-color="#5fb9e6"/>
          <stop offset="0.6" stop-color="#6ccdf0"/>
          <stop offset="1" stop-color="#4aa3dc"/>
        </linearGradient>
        <linearGradient id="townhall-tones" x1="0" y1="0" x2="0" y2="1">
          <stop offset="0" stop-color="#3f6fd0"/>
          <stop offset="0.55" stop-color="#5a6b8a"/>
          <stop offset="0.8" stop-color="#b08a50"/>
          <stop offset="1" stop-color="#c9a25a"/>
        </linearGradient>
        <linearGradient id="library-tones" x1="0" y1="0" x2="0" y2="1">
          <stop offset="0" stop-color="#5e8fd6"/>
          <stop offset="0.4" stop-color="#b9c2cc"/>
          <stop offset="0.7" stop-color="#c8b18a"/>
          <stop offset="1" stop-color="#a88d62"/>
        </linearGradient>
      </defs>
      <rect class="panel-light" width="912" height="419" fill="url(#panel-gradient)"/>
      <polygon class="panel-deep" points="117,0 912,0 912,250 760,345 300,250 300,80" fill="var(--blue-deep)"/>
      <polygon class="hex-frame" points="459,0 610,87 610,262 459,345 297,262 297,87" fill="var(--blue-deep)"/>
      <polygon class="hex-frame" points="760,0 912,87 912,262 760,345 605,262 605,87" fill="var(--blue-deep)"/>
      <g role="img" aria-label="Photo of a Gothic town hall clock tower at dusk">
        <polygon points="459,8 602,91 602,256 459,336 305,256 305,91" fill="url(#townhall-tones)"/>
      </g>
      <g role="img" aria-label="Photo of a domed historic library building under a blue sky">
        <polygon points="760,8 905,91 905,256 760,336 613,256 613,91" fill="url(#library-tones)"/>
      </g>
    </svg>

    <h1 class="headline">
      <span class="lead">Help</span>
      <span class="line">A junior doctor</span>
      <span class="line">Make a</span>
      <span class="big">Big</span>
      <span class="line">Decision</span>
    </h1>
    <p class="tagline">- rate your training!</p>

    <div class="rating" aria-label="Rated 4 out of 5">
      <svg viewBox="0 0 24 24"><path d="M12 2l2.9 6.9 7.1.6-5.4 4.7 1.7 7.1L12 17.6 5.7 21.3l1.7-7.1L2 9.5l7.1-.6z" fill="var(--blue-deep)"/></svg>
      <svg viewBox="0 0 24 24"><path d="M12 2l2.9 6.9 7.1.6-5.4 4.7 1.7 7.1L12 17.6 5.7 21.3l1.7-7.1L2 9.5l7.1-.6z" fill="var(--blue-deep)"/></svg>
      <svg viewBox="0 0 24 24"><path d="M12 2l2.9 6.9 7.1.6-5.4 4.7 1.7 7.1L12 17.6 5.7 21.3l1.7-7.1L2 9.5l7.1-.6z" fill="var(--blue-deep)"/></svg>
      <svg viewBox="0 0 24 24"><path d="M12 2l2.9 6.9 7.1.6-5.4 4.7 1.7 7.1L12 17.6 5.7 21.3l1.7-7.1L2 9.5l7.1-.6z" fill="var(--blue-deep)"/></svg>
      <svg viewBox="0 0 24 24"><path d="M12 3.5l2.5 6 6.3.5-4.8 4.1 1.5 6.2L12 17 6.5 20.3 8 14.1 3.2 10l6.3-.5z" fill="none" stroke="var(--blue-deep)" stroke-width="1.4"/></svg>
    </div>

    <div class="cta-button">Rate and review their training</div>
  </section>
</div>
</body>
</html>
```